Gymnastics and fitness web design

Plavney Gymnastics and fitness centre is opening a new branch in the United States.
Target Audience:
22 to 40 year old people who are not satisfied with their current body figure, shape and size.
and
Our programs
Vexabolt, Sports performance and personal training
DESIGN STYLE:
We want the site to be trendy, edgy and cool. The colors we prefer are blue, black and silver. Th idea is people should get motivated by seeing our website. We don't like adding many text in the design, images oriented design is what we are after.
Contents should be added-
Slider
who we are?
section for our programs
Why us?
Video showing some tutorials
Articles
contact us form with map, Address, Phone number, timings, and social media buttons.

```html
<!DOCTYPE html>
<html lang="en">
<head>
<meta charset="utf-8">
<title>Plavney – Programs</title>
<link href="https://fonts.googleapis.com/css2?family=Russo+One&family=Montserrat:wght@400;500;600&display=swap" rel="stylesheet">
<style>
:root{
  --blue:#1f2fe0;
  --blue-deep:#263399;
  --black:#000;
  --ink:#050507;
  --white:#fff;
  --muted:#c9c9cf;
  --head:"Russo One", sans-serif;
  --body:"Montserrat", sans-serif;
}
*{margin:0;padding:0;box-sizing:border-box}
html,body{width:1200px;height:1200px;overflow:hidden;background:#fff}
.page{position:absolute;left:110px;top:0;width:1225px;height:1500px;transform:scale(.8);transform-origin:0 0;background:var(--black);overflow:hidden;font-family:var(--body);color:var(--white)}
.abs{position:absolute}
.nav{left:0;top:0;width:1225px;height:66px;background:var(--black)}
.brand{left:261px;top:20px;display:flex;align-items:center;gap:9px}
.brand-mark{width:14px;height:14px;background:var(--blue)}
.brand-name{font-family:var(--body);font-weight:600;font-size:22px;color:var(--white);line-height:24px}
.nav-link{top:20px;font-size:12px;font-weight:600;line-height:16px}
.nav-link.active{top:16px;left:758px;width:70px;height:25px;border:1px solid var(--blue);border-radius:3px;text-align:center;line-height:23px}
.hero{left:0;top:66px;width:1225px;height:396px;background:linear-gradient(180deg,#8f8e96 0%,#7a7b8e 55%,#5d6291 100%)}
.hero-photo{left:215px;top:10px;width:290px;height:386px;background:linear-gradient(180deg,#4a3f3e,#2b2426);opacity:.35;border-radius:40% 40% 10% 10%}
.hero-title{left:0;top:96px;width:1225px;text-align:center;font-family:var(--head);font-size:52px;letter-spacing:6px;color:var(--blue)}
.hero-text{left:0;top:164px;width:1225px;text-align:center;font-size:11.5px;font-weight:500;line-height:15px}
.tabs{left:261px;top:297px;width:702px;height:54px;background:rgba(255,255,255,.3);border-radius:4px}
.tab{top:19px;font-family:var(--head);font-size:11px;letter-spacing:1px;transform:translateX(-50%);white-space:nowrap}
.tab-line{left:40px;top:39px;width:115px;height:2px;background:var(--blue)}
.program{left:0;top:462px;width:1225px;height:914px;background:radial-gradient(ellipse at 78% 45%,#3a3434 0%,#1a1719 30%,var(--ink) 60%)}
.h2{font-family:var(--head);font-size:25px;letter-spacing:2.5px;line-height:30px}
.bar{width:73px;height:6px;background:var(--blue)}
.para{font-size:10px;line-height:16px;letter-spacing:-.15px;color:var(--muted)}
.media{left:258px;top:755px;width:351px;height:434px;background:linear-gradient(180deg,#1b1b1d 0%,#6a4a3a 45%,#3b2a24 100%)}
.frame{left:238px;top:772px;width:351px;height:434px;border:1.5px solid var(--white)}
.cta{left:296px;top:1071px;width:245px;height:63px;background:var(--blue);font-family:var(--head);font-size:19px;letter-spacing:2px;text-align:center;line-height:63px}
.feat-title{font-family:var(--head);font-size:13px;letter-spacing:1px}
.feat-text{font-size:10.5px;line-height:16px;color:var(--muted);margin-top:5px}
.icon{left:670px;width:40px;height:40px}
.signup{left:677px;top:1269px;width:172px;height:33px;background:linear-gradient(180deg,#2c3df0,#1a28b8);border-radius:2px;font-size:11px;font-weight:600;text-align:center;line-height:33px}
.next{left:0;top:1376px;width:1225px;height:124px;background:var(--blue-deep)}
</style>
</head>
<body>
<div class="page">
  <header class="nav abs">
    <div class="brand abs">
      <span class="brand-mark"></span>
      <span class="brand-name">Plavney</span>
    </div>
    <span class="nav-link abs" style="left:629px">Home</span>
    <span class="nav-link abs" style="left:697px">About</span>
    <span class="nav-link active abs">Programs</span>
    <span class="nav-link abs" style="left:856px">Blog</span>
    <span class="nav-link abs" style="left:919px">Contact</span>
  </header>

  <section class="hero abs" role="img" aria-label="Athlete leaping against a hazy grey-blue sky">
    <div class="hero-photo abs"></div>
    <h1 class="hero-title abs">PROGRAMS</h1>
    <p class="hero-text abs">Lorem ipsum dolor sit amet, consectetur adipiscing elit. Sed<br>semper massa sit amet urna bibendum dapibus. Nunc eleifend</p>
    <nav class="tabs abs">
      <span class="tab abs" style="left:97px">PROGRAM ONE</span>
      <span class="tab-line abs"></span>
      <span class="tab abs" style="left:265px">PROGRAM TWO</span>
      <span class="tab abs" style="left:431px">PROGRAM THREE</span>
      <span class="tab abs" style="left:600px">PROGRAM FOUR</span>
    </nav>
  </section>

  <section class="program abs" role="img" aria-label="Dark backdrop of an athlete's muscular back">
  </section>

  <h2 class="h2 abs" style="left:260px;top:543px">PROGRAM ONE</h2>
  <div class="bar abs" style="left:260px;top:597px"></div>
  <p class="para abs" style="left:261px;top:627px;width:410px">Lorem ipsum dolor sit amet, consectetur adipisicing elit, sed do eiusmod tempor<br>incididunt ut labore et dolore magna aliqua. Ut enim ad minim veniam, quis<br>nostrud exercitation ullamco laboris nisi ut aliquip ex ea commodo consequat.<br>Duis aute irure dolor in reprehenderit in voluptate velit esse cillum dolore eu<br>fugiat nulla pariatur. Excepteur sint occaecat cupidatat non proident, sunt in</p>

  <div class="media abs" role="img" aria-label="Athlete's back in a sports top, training photo"></div>
  <div class="frame abs"></div>
  <div class="cta abs">WATCH TUTORIAL</div>

  <h2 class="h2 abs" style="left:670px;top:775px">ABOUT PROGRAM ONE</h2>
  <div class="bar abs" style="left:670px;top:829px"></div>
  <p class="para abs" style="left:670px;top:861px;width:340px">Lorem ipsum dolor sit amet, consectetur adipisicing elit, sed do<br>eiusmod tempor incididunt ut labore et dolore magna aliqua. Ut<br>enim ad minim veniam, quis nostrud exercitation ullamco laboris<br>nisi ut aliquip ex ea commodo consequat. Duis aute irure dolor in</p>

  <svg class="icon abs" style="top:970px" viewBox="0 0 40 40" fill="none" stroke="#2233cc" stroke-width="1.6"><ellipse cx="20" cy="18" rx="17" ry="13"/><path d="M20 5v26M8 14c4 2 8 0 12 4M32 14c-4 2-8 0-12 4M14 31l6 6 6-6"/></svg>
  <div class="abs" style="left:732px;top:972px"><div class="feat-title">LOREM IPSUM</div><div class="feat-text">Lorem ipsum dolor sit amet, consectetur<br>adipisicing elit, sed do eiusmod tempor</div></div>

  <svg class="icon abs" style="top:1048px" viewBox="0 0 40 40" fill="none" stroke="#2233cc" stroke-width="1.6"><rect x="5" y="3" width="30" height="35" rx="2"/><circle cx="20" cy="11" r="5"/><path d="M20 11l2-3"/></svg>
  <div class="abs" style="left:732px;top:1043px"><div class="feat-title">LOREM IPSUM</div><div class="feat-text">Lorem ipsum dolor sit amet, consectetur<br>adipisicing elit, sed do eiusmod tempor</div></div>

  <svg class="icon abs" style="top:1115px" viewBox="0 0 40 40" fill="none" stroke="#2233cc" stroke-width="1.6"><path d="M20 34C8 25 3 19 3 12a8 8 0 0 1 17-3 8 8 0 0 1 17 3c0 7-5 13-17 22z"/></svg>
  <div class="abs" style="left:732px;top:1116px"><div class="feat-title">LOREM IPSUM</div><div class="feat-text">Lorem ipsum dolor sit amet, consectetur<br>adipisicing elit, sed do eiusmod tempor</div></div>

  <svg class="icon abs" style="top:1184px" viewBox="0 0 40 40" fill="none" stroke="#2233cc" stroke-width="1.6"><path d="M12 2v6c0 6 4 8 4 13s-6 8-6 17M28 2v6c0 6-4 8-4 13s6 8 6 17M13 28h14M10 38c4-3 7-4 10-4s6 1 10 4"/></svg>
  <div class="abs" style="left:732px;top:1182px"><div class="feat-title">LOREM IPSUM</div><div class="feat-text">Lorem ipsum dolor sit amet, consectetur<br>adipisicing elit, sed do eiusmod tempor</div></div>

  <div class="signup abs">SIGN UP NOW</div>

  <section class="next abs" role="img" aria-label="Blue-toned photo of an athlete for program two">
    <h2 class="h2 abs" style="left:260px;top:81px">PROGRAM TWO</h2>
  </section>

  <svg class="abs" style="left:582px;top:1296px" width="60" height="136" viewBox="0 0 60 136" fill="none" stroke="#fff" stroke-width="1.3"><path d="M30 0v132M2 104l28 28 28-28"/></svg>
</div>
</body>
</html>
```